Redesign of www.tulverhollowarts.example.

I need to take the elements of a PixelGuildry website that was started some time ago but never went live with a website that I now have that is not very compelling. I publish a digital magazine through flipvelo.example and link the magazine to www.tulverhollowarts.example. Boring website.

The PixelGuildry website is: www.brackwaterstageandshow.example. A lively website which is now too narrow in scope. I seek to expand my coverage to include the cultural life of my county.

Here's what I'd like to do.
1. Rename the PixelGuildry website using my url: www.tulverhollowarts.example.
2. Use my tulverhollowarts logo, replacing brackwaterstageandshow.example
3. Break up the large rotating banner on the top into two spaces??? I want to feature my current magazine as the first placement. The space is too wide? Suggestions here appreciated. I also want back issues to be available for viewing.
4. I need flexibility to change headings, etc, so instruction needs to come with the design.
5. I'm thinking of offering blog space to others.

General question. Rather than moving everything over to www.brackwaterstageandshow.example, should we just redesign www.tulverhollowarts.example using the elements on the www.brackwaterstageandshow.example site? Might be an easier way to go.

I'm open to a complete redesign of www.tulverhollowarts.example with the exception of the logo and the spotlight on the magazines,both current and past issues.

I am in the middle of producing the next issue, so the website needs to not change until mid October. I'd like the design to be complete beforehand so we can make the change pretty quickly after the 15th of October.

I've attached covers of our last 2 issues and my logo. I'm open to a change in color with the logo,but not the fonts.

I'm not sure how many pages I'll need and I don't know the difference between coded and uncoded pages...so you can explain to me.

Target Market(s)

Readers who are interested in the arts and culture of the San Francisco Bay Area.

Number of Pages Required

4 page

Font styles to use
Other font styles liked:
• Whatever font is used at www.brackwaterstageandshow.example

Colors

Designer to choose colors to be used in the design.

Requirements
Must have
• Current logo. Color suggestion for the website is fine.Featured space for the magazines. They are placed by my linking them from Flipvelo.example over to my current website. www.brackwaterstageandshow should be used as a template.
• WordPress for blogging and instructions included.
Nice to have
• Nice, bright, fun

```html
<!DOCTYPE html>
<html lang="en">
<head>
<meta charset="utf-8">
<title>Tulver Hollow Arts &amp; Culture</title>
<link href="https://fonts.googleapis.com/css2?family=Roboto:wght@400;500;700;900&family=Roboto+Condensed:wght@400;700&family=Oswald:wght@400;500;700&display=swap" rel="stylesheet">
<style>
:root{
  --navy:#12387a;
  --blue:#1a4fa0;
  --green:#1fae5a;
  --red:#e8453c;
  --coral:#ef5b4f;
  --dark:#2b2b2b;
  --darker:#1f1f1f;
  --ink:#333;
  --muted:#777;
  --light:#f1f1f1;
  --white:#fff;
}
*{box-sizing:border-box;margin:0;padding:0}
html,body{width:1200px;height:3264px;overflow:hidden}
body{font-family:"Roboto",Arial,sans-serif;color:var(--ink);background:var(--white);position:relative}
.ph{display:block}
/* top bar */
.topbar{height:32px;background:var(--navy);display:flex;align-items:center;justify-content:space-between;padding:0 160px;color:var(--white);font-size:12px}
.topbar .phone{display:flex;align-items:center;gap:6px}
.topbar .join{background:var(--green);height:32px;padding:0 20px;display:flex;align-items:center;font-weight:700;font-size:12px;letter-spacing:.5px}
/* header */
.header{height:88px;display:flex;align-items:center;justify-content:space-between;padding:0 160px}
.brand{display:flex;align-items:center;gap:10px;font-family:"Roboto",sans-serif;font-weight:700;font-size:30px;color:var(--navy)}
.brand .dot{width:18px;height:18px;border-radius:50%;background:var(--green)}
.search{display:flex}
.search .field{width:180px;height:30px;border:1px solid #ccc;font-size:12px;color:#999;padding:7px 10px}
.search .go{width:30px;height:30px;background:var(--navy);display:flex;align-items:center;justify-content:center}
/* nav */
.nav{height:24px;background:var(--blue);display:flex;align-items:center;justify-content:space-between;padding:0 160px}
.nav ul{display:flex;list-style:none;gap:28px;color:var(--white);font-size:11px;font-weight:500;text-transform:uppercase}
.social{display:flex;gap:6px}
.social span{width:16px;height:16px;border-radius:50%;background:rgba(255,255,255,.85)}
/* hero */
.hero{height:456px;display:flex;position:relative}
.hero-main{flex:0 0 560px;background:linear-gradient(135deg,#2f6f9e,#1d3c5c 55%,#0e1d2e);position:relative}
.hero-main .name{position:absolute;left:20px;bottom:40px;color:var(--white);font-family:"Oswald",sans-serif;font-size:46px;font-weight:500;line-height:1}
.hero-side{flex:1;display:grid;grid-template-columns:1fr 1fr;grid-template-rows:230px 226px}
.hero-art{background:linear-gradient(160deg,#c9c5be,#6e6a66)}
.hero-print{background:linear-gradient(160deg,#efeeea,#b9b6b0);position:relative}
.hero-print .label{position:absolute;left:18px;bottom:22px;background:var(--darker);color:var(--white);font-family:"Oswald",sans-serif;font-size:22px;padding:4px 10px}
.hero-text{background:#f7f5f0;padding:24px 22px;position:relative}
.hero-text .big{font-family:"Oswald",sans-serif;font-size:34px;color:var(--darker);font-weight:700;line-height:1.05}
.hero-text .sub{font-size:13px;color:var(--ink);margin-top:10px;line-height:1.4}
.hero-musica{background:linear-gradient(160deg,#3a3a3a,#111);position:relative}
.hero-musica .label{position:absolute;left:18px;bottom:22px;color:var(--white);font-family:"Oswald",sans-serif;font-size:24px;background:rgba(0,0,0,.6);padding:4px 10px}
/* tagline */
.tagline{height:100px;background:var(--green);display:flex;align-items:center;justify-content:center;text-align:center;color:var(--white);font-family:"Roboto Condensed",sans-serif;font-weight:700;font-size:30px;line-height:1.15;text-transform:uppercase}
/* welcome */
.welcome{height:532px;padding:56px 160px 0;display:flex;gap:40px}
.welcome-copy{flex:0 0 400px}
.welcome-copy h2{font-size:18px;font-weight:700;text-transform:uppercase;color:var(--darker);padding-bottom:8px;border-bottom:2px solid var(--red);display:inline-block;margin-bottom:16px}
.welcome-copy p{font-size:11.5px;line-height:1.6;color:var(--muted);margin-bottom:12px}
.btn{display:inline-block;background:var(--red);color:var(--white);font-size:11px;font-weight:700;padding:9px 16px;text-transform:uppercase}
.welcome-devices{flex:1;background:radial-gradient(ellipse at center,#dfe3e8,#fff 70%);margin-top:10px;height:400px}
/* magazine band */
.mag{height:148px;background:var(--dark);color:var(--white);text-align:center;padding-top:18px}
.mag .kicker{font-family:"Oswald",sans-serif;font-size:22px;letter-spacing:1px;text-transform:uppercase}
.mag .title{font-family:"Oswald",sans-serif;font-size:46px;line-height:1;text-transform:uppercase;font-weight:500}
.mag .join{display:inline-block;border:1px solid var(--white);font-size:11px;font-weight:700;padding:5px 12px;margin-top:8px}
/* events */
.events{padding:40px 160px 0;height:828px}
.section-title{text-align:center;font-family:"Roboto Condensed",sans-serif;font-weight:700;font-size:26px;text-transform:uppercase;color:var(--darker);margin-bottom:26px}
.ev-grid{display:grid;grid-template-columns:430px 430px;gap:20px}
.ev-card .img{height:230px}
.ev-cap{background:var(--light);padding:10px 12px;font-size:11px;line-height:1.45;color:var(--muted);height:70px}
.ev-cap b{display:block;color:var(--darker);font-size:12px}
.ev-pair{display:grid;grid-template-columns:1fr 1fr;gap:10px}
.ev-row{display:flex;background:var(--light);height:145px;margin-bottom:10px}
.ev-row .img{flex:0 0 140px;height:145px}
.ev-row .ev-cap{height:auto;flex:1}
/* performers */
.performers{height:352px;background:linear-gradient(90deg,var(--red),var(--coral));color:var(--white);text-align:center;padding-top:26px;position:relative}
.performers .section-title{color:var(--white);margin-bottom:12px}
.avatar{width:74px;height:74px;border-radius:50%;background:linear-gradient(135deg,#f4c6b8,#9a6a5a);border:3px solid var(--white);margin:0 auto}
.performers .who{font-size:14px;font-weight:700;margin:8px 0 6px}
.performers p{font-size:11.5px;line-height:1.5;width:760px;margin:0 auto}
.performers .social{justify-content:center;margin:12px 0}
.btn-white{display:inline-block;background:var(--darker);color:var(--white);font-size:11px;font-weight:700;padding:8px 16px;text-transform:uppercase}
.arrow{position:absolute;top:160px;width:30px;height:30px;border-radius:50%;background:var(--white);display:flex;align-items:center;justify-content:center}
.arrow.left{left:130px}.arrow.right{right:130px}
/* reviews */
.reviews{height:520px;padding:40px 160px 0}
.rev-grid{display:grid;grid-template-columns:repeat(3,1fr);gap:30px;margin-top:44px}
.rev{background:var(--light);padding:48px 22px 22px;text-align:center;position:relative;height:200px}
.rev .face{position:absolute;top:-32px;left:50%;margin-left:-32px;width:64px;height:64px;border-radius:50%;border:3px solid var(--white);background:linear-gradient(135deg,#c7b8a8,#6e5c4e)}
.rev p{font-size:11.5px;line-height:1.55;color:var(--muted);font-style:italic}
.rev .by{font-size:12px;font-weight:700;color:var(--darker);margin-top:10px}
/* footer */
.footer{position:absolute;left:0;top:3080px;width:1200px;height:184px;background:var(--darker);color:#bbb;text-align:center;padding-top:40px}
.footer ul{display:flex;justify-content:center;list-style:none;gap:24px;font-size:11px;text-transform:uppercase}
.footer .social{justify-content:center;margin:22px 0}
.footer .social span{width:22px;height:22px;background:#555}
.footer small{font-size:11px}
</style>
</head>
<body>
<div class="topbar">
  <div class="phone"><svg width="12" height="12" viewBox="0 0 24 24"><path fill="#fff" d="M6.6 10.8a15 15 0 0 0 6.6 6.6l2.2-2.2c.3-.3.7-.4 1-.2 1.1.4 2.3.6 3.6.6.6 0 1 .4 1 1V20c0 .6-.4 1-1 1C10.6 21 3 13.4 3 4c0-.6.4-1 1-1h3.5c.6 0 1 .4 1 1 0 1.3.2 2.5.6 3.6.1.3 0 .7-.2 1z"/></svg>1-555-014-2290</div>
  <div class="join">JOIN US</div>
</div>
<header class="header">
  <div class="brand"><span class="dot"></span>tulverhollowarts</div>
  <div class="search"><div class="field">Search here</div><div class="go"><svg width="14" height="14" viewBox="0 0 24 24"><circle cx="10" cy="10" r="6" stroke="#fff" stroke-width="2.5" fill="none"/><path d="M15 15l6 6" stroke="#fff" stroke-width="2.5"/></svg></div></div>
</header>
<nav class="nav">
  <ul><li>Home</li><li>What We Do</li><li>Contributors</li><li>Advertising</li><li>Concert Hall</li><li>Art News</li><li>Contact Us</li></ul>
  <div class="social"><span></span><span></span><span></span><span></span></div>
</nav>
<section class="hero">
  <div class="hero-main" role="img" aria-label="Photo of a cellist performing by the water">
    <div class="name">WREN<br>HALLOWAY</div>
  </div>
  <div class="hero-side">
    <div class="hero-art" role="img" aria-label="Photo of a painter at work in a studio"></div>
    <div class="hero-print" role="img" aria-label="Photo of a letterpress printmaker with prints">
      <div class="label">HOLLIS BRANDT</div>
    </div>
    <div class="hero-text">
      <div class="big">OREN CASTLEBURY</div>
      <div class="sub">Internationally celebrated woodcut &amp; letterpress artist</div>
    </div>
    <div class="hero-musica" role="img" aria-label="Photo of a chamber ensemble on stage">
      <div class="label">MUSICA TULVER:</div>
    </div>
  </div>
</section>
<section class="tagline">Written for Tulverites and their friends<br>who love the arts</section>
<section class="welcome">
  <div class="welcome-copy">
    <h2>Welcome to tulverhollowarts</h2>
    <p>Our county is home to painters, players, poets and makers of every kind. Each month we gather their stories, studios and stages into one lively magazine that readers can browse from any screen, at home or on the go.</p>
    <p>Find interviews with working artists, reviews of the latest shows, gallery openings and concert notes. Back issues stay close at hand, so a favourite feature is never more than a click away whenever you want to revisit it.</p>
    <p>Share the magazine with friends, join our mailing list and tell us what you would like to see next.</p>
    <span class="btn">Read More</span>
  </div>
  <div class="welcome-devices" role="img" aria-label="Magazine pages shown on a desktop, laptop, tablet and phone"></div>
</section>
<section class="mag">
  <div class="kicker">Tulver Hollow Arts &amp; Culture</div>
  <div class="title">Online Magazine</div>
  <span class="join">JOIN NOW ▸</span>
</section>
<section class="events">
  <h2 class="section-title">Events Listings</h2>
  <div class="ev-grid">
    <div class="ev-card">
      <div class="img" style="background:linear-gradient(135deg,#f2b33d,#3a72b8)" role="img" aria-label="Painted landscape poster for a spring exhibit"></div>
      <div class="ev-cap"><b>Spring Landscapes Exhibit</b>Fresh paintings of hills and shoreline by local artists, with an opening reception and live music.<br>Gallery Row, 12 April</div>
    </div>
    <div class="ev-card">
      <div class="ev-pair">
        <div class="img" style="background:linear-gradient(135deg,#8a9aa6,#3b4650)" role="img" aria-label="Photo of a choir rehearsing outdoors"></div>
        <div class="img" style="background:linear-gradient(135deg,#d8413a,#e6b52c)" role="img" aria-label="Colourful theatre and film posters"></div>
      </div>
      <div class="ev-cap"><b>Choir in the Garden</b>An afternoon of open air song followed by a poster show of classic stage and film art.<br>Civic Lawn, 19 April</div>
    </div>
    <div class="ev-card">
      <div class="img" style="background:linear-gradient(135deg,#5a2b1e,#c9712a)" role="img" aria-label="Tulver Symphony season poster with orchestra"></div>
      <div class="ev-cap"><b>Tulver Symphony Season</b>Where great music comes alive: the new season opens with a program of beloved works.<br>Concert Hall, 3 May</div>
    </div>
    <div class="ev-card">
      <div class="ev-row">
        <div class="img" style="background:linear-gradient(135deg,#e35a2a,#f1b02d)" role="img" aria-label="Poster for music and more on Mt. Corvale"></div>
        <div class="ev-cap"><b>Music and More on Mt. Corvale</b>Summer evenings of folk, jazz and story on the mountain amphitheater.<br>Mt. Corvale, 10 May</div>
      </div>
      <div class="ev-row">
        <div class="img" style="background:linear-gradient(135deg,#a2483c,#e3c9a4)" role="img" aria-label="Photo of a string quartet"></div>
        <div class="ev-cap"><b>Evening String Quartet</b>Intimate chamber music in the old library reading room.<br>Library Hall, 17 May</div>
      </div>
    </div>
  </div>
</section>
<section class="performers">
  <h2 class="section-title">Performers Profile</h2>
  <div class="avatar" role="img" aria-label="Portrait of the featured performer"></div>
  <div class="who">Dorian Pell</div>
  <p>A pianist and composer raised in the valley, Dorian has played halls across the country and returns home each season to teach, record and perform with friends from the local scene.</p>
  <div class="social"><span></span><span></span><span></span><span></span></div>
  <span class="btn-white">View Profile</span>
  <div class="arrow left"><svg width="12" height="12" viewBox="0 0 24 24"><path d="M15 4l-8 8 8 8" stroke="#e8453c" stroke-width="3" fill="none"/></svg></div>
  <div class="arrow right"><svg width="12" height="12" viewBox="0 0 24 24"><path d="M9 4l8 8-8 8" stroke="#e8453c" stroke-width="3" fill="none"/></svg></div>
</section>
<section class="reviews">
  <h2 class="section-title">User Reviews</h2>
  <div class="rev-grid">
    <div class="rev"><div class="face" role="img" aria-label="Reader portrait"></div><p>“I look forward to every issue. The interviews feel personal and I always discover a new gallery or show to visit.”</p><div class="by">Mara Quinlan</div></div>
    <div class="rev"><div class="face" role="img" aria-label="Reader portrait"></div><p>“Beautiful layouts and thoughtful writing. It is the best guide to what is happening in the arts around here.”</p><div class="by">Teo Aldridge</div></div>
    <div class="rev"><div class="face" role="img" aria-label="Reader portrait"></div><p>“Reading back issues on my tablet is easy, and the event listings have filled my weekends with music.”</p><div class="by">Ines Varga</div></div>
  </div>
</section>
<footer class="footer">
  <ul><li>Home</li><li>What We Do</li><li>Contributors</li><li>Advertising</li><li>Concert Hall</li><li>Art News</li><li>Contact Us</li></ul>
  <div class="social"><span></span><span></span><span></span><span></span><span></span></div>
  <small>Copyright © www.tulverhollowarts.example. All rights reserved.</small>
</footer>
</body>
</html>
```